Neurosurgeon office (Cranial and Spinal diseases)

Need paper itens like:

Business card
Mail
Prescription (A4)
Receipt
Brochure (for informations like disease I treat with place for photo)

My name: Rodrigo Menezes Tavora

PS: need a plain or 3D logo based on my signature

Thanks for all attention !

Preciso de artigos de papelaria:
Cartão de visita
Envelope
Receituário (A4)
Recibo médico
Panfleto (com informações como doenças que trato com lugar para foto)

Meu nome: Rodrigo Menezes Tavora

OBS: Gostaria de um logo baseado na minha rubrica (envio foto abaixo)

Muito obrigado pela atenção !

Hello designers, First, I want to thank you all for helping me with my project. Received some examples, I'm waiting for changes, etc. I had an idea that could do some nice works ... You can try classic style, using soft colors like: White/Black Carolina blue / Air Superiority Blue (http://en.tintopedia.org/wiki/Category:Shades_of_blue) Jungle green (http://en.tintopedia.org/wiki/Category:Shades_of_green) Apricot (http://en.tintopedia.org/wiki/Category:Shades_of_orange) About Logo, you can try logo itself with shapes outside, 3D (like inside a cube or something original) or 2D or a drawing reminding my signature with brain and spine (like brain on C and Spine on F line) or both (like drawings of brain and spine along with the original signature). I'm certain about good works. Would like to receive something original, not a padronized medical paper examples (like using eletrocardiogram, stetoscope, etc ...) ... you can google things that remind my work as brain, neuron, spine, etc ... Thank you all for the attention, certain that someone will achieve my desire for a brilliant work ! Best Regards from Brazil. Rodrigo Tavora PS: going to try to post a JPEG with some examples that you can try on project.

Reason: Received 4 designs under consideration only ... Updated informations today so it's easier to designers to do something that I will like Thanks for all attention ! Best Regards Rodrigo

Reason: No designs that match my search yet

Reason: Waiting for projects

Target Market(s)

Patients with spinal and brain diseases

Industry/Entity Type

Business

Font styles to use
Script
Other font styles liked:
• Times New Roman, Trajan Pro, Palatino LInotype

Colors
33a6d7
add136
3176b5
f9ba93
aaaaaa
f04a50

Requirements
Must have
• The best design I saw on google was like this one ... this is like the logo I want for me ...

https://q7vm3rbtwzk9xe.imgvaultcdn.net/Rb8Kp2TzW4mQx7Lsy_HnVdE91aQ=/fit-in/500x370/http%3A%2F%2Fp4j2wvrkzq8hs.imgvaultcdn.net%2Fdesigns%2F58310947~2b4e90c7a1d3f865b07e12c94f6a3d58b71c0e92-original

Use 2 or more colors with white ... like degradée (different tones of same color)

Nice to have
• Can use logo mixed with RODRIGO TAVORA (and NEUROCIRURGIA below)
Should not have
• Stetoscopes, eletrocradiogram traces

```html
<!DOCTYPE html>
<html lang="pt">
<head>
<meta charset="utf-8">
<title>Rodrigo Menezes Tavora — Papelaria</title>
<link rel="stylesheet" href="https://fonts.googleapis.com/css2?family=Sorts+Mill+Goudy&display=swap">
<style>
  :root {
    --backdrop: #efefef;
    --paper: #ffffff;
    --band-light: #e4e8ea;
    --band-mid: #c9d0d4;
    --band-shine: #f6f7f8;
    --flap: #dfe4e6;
    --rule: #9a9a9a;
    --ink: #1a1a1a;
    --mark: #4a4a4a;
    --ornament: #c4c4c4;
    --window-line: #b9bdc0;
  }
  * { box-sizing: border-box; margin: 0; padding: 0; }
  html, body { width: 1057px; height: 1200px; overflow: hidden; background: var(--backdrop); }
  .sheet-board { position: relative; width: 1057px; height: 1200px; font-family: "Sorts Mill Goudy", "Palatino Linotype", serif; color: var(--ink); }
  .item { position: absolute; background: var(--paper); overflow: hidden; box-shadow: 0 2px 6px rgba(0,0,0,.18); }
  .item svg.bands { position: absolute; inset: 0; width: 100%; height: 100%; }
  .mark-square { position: absolute; background: var(--mark); border-radius: 4px; }
  .mark-name { position: absolute; font-size: 7px; line-height: 1; color: var(--ink); white-space: nowrap; }

  .business-card { left: 151px; top: 194px; width: 300px; height: 194px; border-radius: 14px; }
  .business-card .mark-square { left: 14px; top: 22px; width: 40px; height: 66px; }
  .business-card .mark-name { left: 10px; top: 93px; }
  .business-card .card-name { position: absolute; left: 80px; top: 80px; width: 196px; height: 24px; line-height: 24px; text-align: center; font-size: 16px; white-space: nowrap; }
  .business-card .rule { position: absolute; left: 89px; width: 178px; height: 1px; background: var(--rule); }
  .business-card .rule.top { top: 76px; }
  .business-card .rule.bottom { top: 107px; }
  .business-card .ornament { position: absolute; left: 148px; width: 60px; height: 5px; background: var(--ornament); border-radius: 3px; }
  .business-card .ornament.top { top: 68px; }
  .business-card .ornament.bottom { top: 112px; }

  .envelope { left: 474px; top: 131px; width: 423px; height: 259px; }
  .envelope .flap { position: absolute; left: 0; top: 0; width: 100%; height: 45px; background: var(--flap); border-bottom: 1px solid var(--band-mid); }
  .envelope .mark-square { left: 26px; top: 66px; width: 34px; height: 58px; }
  .envelope .mark-name { left: 12px; top: 129px; }
  .envelope .address-window { position: absolute; left: 210px; top: 159px; width: 184px; height: 67px; border: 1px solid var(--window-line); border-radius: 6px; }

  .letterhead { left: 155px; top: 403px; width: 458px; height: 689px; }
  .letterhead .mark-square { left: 60px; top: 66px; width: 62px; height: 97px; border-radius: 6px; }
  .letterhead .sheet-name { position: absolute; left: 25px; top: 170px; font-size: 11px; line-height: 1; white-space: nowrap; }

  .receipt { left: 653px; top: 405px; width: 241px; height: 364px; }
  .receipt .mark-square { left: 28px; top: 25px; width: 26px; height: 44px; border-radius: 3px; }
  .receipt .sheet-name { position: absolute; left: 62px; top: 44px; font-size: 7.5px; line-height: 1; white-space: nowrap; }
</style>
</head>
<body>
<main class="sheet-board">

  <section class="item business-card" aria-label="Cartão de visita">
    <svg class="bands" viewBox="0 0 300 194" preserveAspectRatio="none" aria-hidden="true">
      <polygon points="0,0 82,0 42,194 0,194" fill="var(--band-light)"/>
      <polygon points="58,0 76,0 38,194 24,194" fill="var(--band-shine)"/>
      <polygon points="76,0 82,0 42,194 38,194" fill="var(--band-mid)"/>
    </svg>
    <div class="mark-square"></div>
    <span class="mark-name">Rodrigo Tavora</span>
    <div class="ornament top" role="img" aria-label="Ornamento decorativo acima do nome"></div>
    <div class="rule top"></div>
    <p class="card-name">Rodrigo Menezes Tavora</p>
    <div class="rule bottom"></div>
    <div class="ornament bottom" role="img" aria-label="Ornamento decorativo abaixo do nome"></div>
  </section>

  <section class="item envelope" aria-label="Envelope">
    <svg class="bands" viewBox="0 0 423 259" preserveAspectRatio="none" aria-hidden="true">
      <polygon points="0,45 108,45 52,259 0,259" fill="var(--band-light)"/>
      <polygon points="82,45 100,45 48,259 34,259" fill="var(--band-shine)"/>
      <polygon points="100,45 108,45 52,259 48,259" fill="var(--band-mid)"/>
    </svg>
    <div class="flap"></div>
    <div class="mark-square"></div>
    <span class="mark-name">Rodrigo Tavora</span>
    <div class="address-window"></div>
  </section>

  <section class="item letterhead" aria-label="Receituário A4">
    <svg class="bands" viewBox="0 0 458 689" preserveAspectRatio="none" aria-hidden="true">
      <polygon points="0,0 168,0 46,689 0,689" fill="var(--band-light)"/>
      <polygon points="0,0 70,0 0,420" fill="var(--band-shine)"/>
      <polygon points="72,0 148,0 40,689 14,689" fill="var(--band-shine)"/>
      <polygon points="148,0 168,0 46,689 40,689" fill="var(--band-mid)"/>
    </svg>
    <div class="mark-square"></div>
    <p class="sheet-name">Rodrigo Menezes Tavora</p>
  </section>

  <section class="item receipt" aria-label="Recibo médico">
    <div class="mark-square"></div>
    <p class="sheet-name">Rodrigo Menezes Tavora</p>
  </section>

</main>
</body>
</html>
```